Thornwell tri-fold DL Flyer Clinic

Thornwell is an award-winning organisation providing dynamic and creative ways for children, young people, adults and families to make positive change and achieve fulfilling lives. We have a general psychology clinic and also offer KVRP services for people with high and intensive needs.  We have recently opened our purpose fitted clinic and are now looking to create a flyer to use in our promotions of the clinic.
We are after an a4 colour double sided flyer in a tri fold to DL format.   We are looking for a design that is simple and dynamic whilst keeping in line with our branding.  I envisage this brochure could use some photos of the space (in a dynamic way) and potentially some illustration.  I have attached a number of files to provide further background and also images of the space that could be used.   I have also attached the draft text for the flyer and current map we use to send to clients.
The winning design will need to be hi-res and ready for print.

- Poppins

```html
<!DOCTYPE html>
<html lang="en">
<head>
<meta charset="utf-8">
<title>Thornwell tri-fold DL flyer</title>
<link href="https://fonts.googleapis.com/css2?family=Poppins:wght@300;400;500;600&display=swap" rel="stylesheet">
<style>
:root{
  --rose:#a98a7c;
  --rose-dark:#8f7064;
  --blush:#efe0d7;
  --sage:#5e7868;
  --ink:#3a3433;
  --white:#ffffff;
  --page:#e4e2e1;
}
*{box-sizing:border-box;margin:0;padding:0}
html,body{width:1200px;height:3600px;overflow:hidden;background:var(--page);font-family:"Poppins",sans-serif;color:var(--ink)}
.spread{position:absolute;left:40px;width:1120px;height:792px;display:grid;grid-template-columns:repeat(3,1fr);box-shadow:0 6px 24px rgba(0,0,0,.18);background:var(--white);overflow:hidden}
.spread--outside{top:960px}
.spread--inside{top:1848px}
.panel{position:relative;overflow:hidden}
.photo{position:absolute;left:0;right:0}
.heading{font-weight:500;font-size:22px;line-height:1.2}
.brand{display:flex;align-items:center;gap:8px;font-weight:600;font-size:22px;color:var(--sage)}
.brand__dot{width:14px;height:14px;border-radius:50%;background:var(--rose)}

/* outside: about */
.about__text{position:absolute;top:0;left:0;right:0;height:500px;background:var(--rose);color:var(--white);padding:34px 30px}
.about__text p{font-size:12px;line-height:1.65;font-weight:300;margin-top:14px}
.about__photo{top:500px;height:292px;background:linear-gradient(135deg,#c9d3d6,#9aa5a6 55%,#e3e6e4)}

/* outside: directions */
.directions__head{position:absolute;top:0;left:0;right:0;height:72px;background:var(--sage);color:var(--white);padding:14px 22px}
.directions__head h3{font-size:15px;font-weight:500}
.directions__head p{font-size:10px;font-weight:300}
.directions__map{top:72px;height:270px;background:linear-gradient(160deg,#f2efe9,#dfe5e0 60%,#e9ddd6)}
.directions__building{top:342px;height:200px;background:linear-gradient(180deg,#b9cfe0,#c9b9a8 60%,#8e8278)}
.directions__contact{position:absolute;top:542px;left:0;right:0;bottom:0;background:var(--blush);padding:18px 22px}
.directions__address{font-size:12px;line-height:1.5;font-weight:500}
.directions__phone{display:flex;align-items:center;gap:8px;margin-top:10px;font-size:24px;font-weight:600;color:var(--rose-dark)}
.directions__links{font-size:11px;margin-top:6px}
.directions__small{font-size:9px;line-height:1.45;margin-top:10px;color:#6b605d}

/* outside: cover */
.cover__photo{top:0;height:430px;background:linear-gradient(150deg,#f4f4f4,#b6b1ae 45%,#7d7673)}
.cover__brand{position:absolute;top:30px;right:26px;background:var(--white);padding:8px 14px}
.cover__band{position:absolute;top:430px;left:0;right:0;bottom:0;background:var(--rose);color:var(--white);padding:40px 30px}
.cover__title{font-size:30px;font-weight:400;line-height:1.2}
.cover__sub{font-size:18px;font-weight:300;line-height:1.35;margin-top:16px}
.cover__url{position:absolute;bottom:34px;left:30px;font-size:13px;font-weight:400}

/* inside: services */
.services{background:var(--blush);padding:30px 28px}
.services__intro{font-size:12px;font-weight:600;margin:10px 0 12px;line-height:1.4}
.list{list-style:none}
.list li{font-size:12px;line-height:22px;padding-left:14px;position:relative}
.list li::before{content:"";position:absolute;left:0;top:9px;width:5px;height:5px;border-radius:50%;background:currentColor}

/* inside: approaches */
.approaches__photo{top:0;height:330px;background:linear-gradient(135deg,#f3f3f1,#c8c6c2 50%,#8f8c88)}
.approaches__brand{position:absolute;top:120px;left:26px;background:var(--white);padding:8px 14px}
.approaches__box{position:absolute;top:330px;left:0;right:0;bottom:0;background:var(--sage);color:var(--white);padding:26px 28px}
.approaches__box .list li{font-size:11.5px;line-height:21px}

/* inside: assessments */
.assess__box{position:absolute;top:0;left:0;right:0;height:400px;background:var(--rose);color:var(--white);padding:30px 28px}
.assess__box .list{margin-top:16px}
.assess__photo{top:400px;height:392px;background:linear-gradient(160deg,#e9e9e7,#b5b8b7 50%,#6f7474)}
</style>
</head>
<body>

<section class="spread spread--outside">
  <div class="panel about">
    <div class="about__text">
      <h2 class="heading">About Thornwell:</h2>
      <p>Thornwell is an award-winning organisation and a B-Corporation, providing dynamic and creative ways for children, young people, adults and families to make positive change and achieve fulfilling lives. In our new purpose fitted clinic, we provide a safe space for confidential psychology, counselling, and support services. We also offer KVRP services for people with high and intensive needs.</p>
      <p>Our team has extensive experience working with mental health issues and complex disability, and people who are neurodivergent to live their best lives. We provide quality, evidence informed services to adults and children with complex needs along with their families and networks.</p>
    </div>
    <div class="photo about__photo" role="img" aria-label="Photos of the clinic play and therapy rooms"></div>
  </div>

  <div class="panel directions">
    <div class="directions__head">
      <h3>How to get to Thornwell</h3>
      <p>Harbourline Building, 42 Fenwick Lane, Marlow</p>
    </div>
    <div class="photo directions__map" role="img" aria-label="Street map showing the clinic location"></div>
    <div class="photo directions__building" role="img" aria-label="Photo of the Harbourline Building exterior"></div>
    <div class="directions__contact">
      <p class="directions__address">Harbourline Building<br>42 Fenwick Lane, Marlow VIC 3999</p>
      <p class="directions__phone">
        <svg width="20" height="20" viewBox="0 0 24 24" aria-hidden="true"><path fill="currentColor" d="M6.6 10.8a15.1 15.1 0 0 0 6.6 6.6l2.2-2.2c.3-.3.7-.4 1-.2 1.1.4 2.3.6 3.6.6.6 0 1 .4 1 1V20c0 .6-.4 1-1 1A17 17 0 0 1 3 4c0-.6.4-1 1-1h3.5c.6 0 1 .4 1 1 0 1.3.2 2.5.6 3.6.1.3 0 .7-.2 1z"/></svg>
        03 9000 1234
      </p>
      <p class="directions__links">info@thornwell.com.au &nbsp;|&nbsp; www.thornwell.com.au</p>
      <p class="directions__small">Free parking is available on site, and the clinic is a short walk from local tram and bus stops.</p>
    </div>
  </div>

  <div class="panel cover">
    <div class="photo cover__photo" role="img" aria-label="Soft black and white photo of a calm therapy setting"></div>
    <div class="cover__brand"><span class="brand"><span class="brand__dot"></span>Thornwell</span></div>
    <div class="cover__band">
      <h1 class="cover__title">Positive Behaviour Support Services</h1>
      <p class="cover__sub">for adults and children with multiple and complex needs</p>
      <p class="cover__url">www.thornwell.com.au</p>
    </div>
  </div>
</section>

<section class="spread spread--inside">
  <div class="panel services">
    <h2 class="heading">Our Services:</h2>
    <p class="services__intro">We can support children, adolescents and adults experiencing:</p>
    <ul class="list">
      <li>Anxiety</li><li>Panic Attacks</li><li>Phobias</li><li>Depression</li><li>Complex Trauma</li>
      <li>Post-Traumatic Stress Disorder (PTSD)</li><li>Autism Spectrum Disorder (ASD)</li><li>Learning Disorders</li>
      <li>Intellectual Disability</li><li>Dual Disability</li><li>Attention Deficit Hyperactivity Disorder (ADHD)</li>
      <li>Bipolar Disorder</li><li>Schizophrenia</li><li>Obsessive-Compulsive Disorder</li><li>Personality Disorders</li>
      <li>Challenging Behaviours</li><li>Relationship Issues</li><li>LGBTQIA+ and Sexuality Issues</li>
      <li>Drug and Alcohol Issues</li><li>Addictions</li><li>Grief and Loss</li><li>Harassment/Workplace Stress</li>
      <li>Bullying</li><li>Body Image and Self Esteem</li><li>Life Transitions</li><li>Chronic Illness</li>
    </ul>
  </div>

  <div class="panel approaches">
    <div class="photo approaches__photo" role="img" aria-label="Photo of the clinic reception and hallway"></div>
    <div class="approaches__brand"><span class="brand"><span class="brand__dot"></span>Thornwell</span></div>
    <div class="approaches__box">
      <h2 class="heading">Therapeutic Approaches:</h2>
      <ul class="list" style="margin-top:14px">
        <li>Cognitive Behavioural Therapy (CBT)</li><li>Acceptance and Commitment Therapy (ACT)</li>
        <li>Dialectical Behavioural Therapy (DBT)</li><li>Mindfulness Based Therapies</li>
        <li>Compassion Focussed Therapies</li><li>Eye Movement Desensitisation and Reprocessing (EMDR)</li>
        <li>Schema Therapy</li><li>Internal Family Systems Therapy</li><li>Motivational Interviewing</li>
        <li>Narrative Therapy</li><li>Art Therapy and Expressive Therapies</li><li>Play Therapy</li>
      </ul>
    </div>
  </div>

  <div class="panel assess">
    <div class="assess__box">
      <h2 class="heading">Psychological Assessments for Children, Adolescents and Adults:</h2>
      <ul class="list">
        <li>Cognitive Assessments (IQ Testing)</li><li>Autism Assessments (ADOS-2)</li>
        <li>Specific Learning Disorder Assessments</li><li>Intellectual Disability Assessments</li>
        <li>Memory Assessments</li><li>Personality Assessments</li><li>Vocational Assessments</li>
        <li>Mood Assessments</li><li>Behavioural Assessments</li>
      </ul>
    </div>
    <div class="photo assess__photo" role="img" aria-label="Photo of the clinic waiting room with chairs"></div>
  </div>
</section>

</body>
</html>
```